Real Estate Agent "Team" Ad that will go into the local newspaper

We need an ad design for the local newspaper. I've attached a copy of our last ad. We would like a little different design (use same content). The size is 4 inches tall x 6.5 inches wide. We would like to include our two photos. Keep it CLEAN and simple. We are a Mercer Island, Washington-based mother/daughter Fenwick Dalton real estate team focused exclusively on Mercer Island. The graphic design should reinforce the tone of warm/approachable, while clean and polished. The feel should be on-trend, current and clean/tight/contemporary. Should appeal to a high net worth consumer. The design should tell potential clients that Greta & Lydia are the premier, trusted team of advisors that informed buyers and sellers turn to for any residential real estate opportunities on Mercer Island.

Target Market(s)

Mercer Island Residents (past and potential customers). High-end, sophisticated Buyers.

Industry/Entity Type

Real Estate Agent

Font styles to use
Serif
Sans Serif

Colors
959595
5c5c5c
474747

Requirements
Must have
• Greta Haskins and Lydia Haskins Photos. Personal Logo. Fenwick Dalton Rusk logo. Please keep colors simple (Black and White) with the exception of our photos and logos.
Nice to have
• Please keep Greta and Lydia Photos equal in size. This is a partnership.
Should not have
• No additional photos of houses or keys.

```html
<!DOCTYPE html>
<html lang="en">
<head>
<meta charset="utf-8">
<title>Greta Haskins &amp; Lydia Haskins Marlow Real Estate</title>
<link rel="stylesheet" href="https://fonts.googleapis.com/css2?family=Arimo:wght@400;700&display=swap">
<style>
  :root {
    --ink: #474747;
    --mid: #5c5c5c;
    --soft: #959595;
    --band: #474747;
    --white: #ffffff;
    --accent: #9cc43c;
  }
  * { margin: 0; padding: 0; box-sizing: border-box; }
  html, body { width: 738px; height: 1200px; overflow: hidden; background: var(--white); }
  body { font-family: "Arimo", Arial, sans-serif; color: var(--ink); }
  .ad { position: relative; width: 738px; height: 1200px; background: var(--white); }

  .brand { position: absolute; left: 118px; top: 72px; display: flex; align-items: center; gap: 22px; }
  .brand__square { width: 86px; height: 86px; background: var(--accent); }
  .brand__name { color: var(--soft); font-weight: 700; }
  .brand__line { display: block; font-size: 36px; line-height: 44px; letter-spacing: 0.5px; }
  .brand__tag { display: block; margin-top: 10px; padding-top: 8px; border-top: 2px solid var(--soft);
    font-size: 17px; letter-spacing: 17px; }

  .band { position: absolute; left: 0; top: 285px; width: 738px; height: 553px; background: var(--band); }
  .band__headline { margin-top: 18px; text-align: center; color: var(--white); font-weight: 700;
    font-size: 41px; line-height: 48px; }
  .agents { position: absolute; left: 63px; top: 145px; display: flex; gap: 40px; }
  .agent { width: 287px; text-align: center; color: var(--white); }
  .agent__photo { width: 287px; height: 313px; border-radius: 6px; }
  .agent__photo--greta { background: radial-gradient(circle at 50% 45%, #e6e2de 0%, #bdb6b0 55%, #8c8782 100%); }
  .agent__photo--lydia { background: radial-gradient(circle at 50% 45%, #d9c3b6 0%, #6e5d55 55%, #3a3533 100%); }
  .agent__name { margin-top: 15px; font-size: 22px; font-weight: 700; line-height: 28px; }
  .agent__phone { font-size: 23px; line-height: 32px; }

  .tagline { position: absolute; left: 63px; top: 888px; font-size: 41px; line-height: 47px;
    font-weight: 700; color: var(--ink); letter-spacing: -0.3px; }
  .contact { position: absolute; left: 63px; top: 1068px; width: 324px; padding-top: 10px;
    border-top: 2px dotted var(--soft); color: var(--soft); font-weight: 700; font-size: 21px;
    line-height: 32px; letter-spacing: 1.4px; }
  .broker { position: absolute; left: 489px; top: 1016px; width: 187px; height: 122px;
    display: flex; flex-direction: column; align-items: center; justify-content: center; gap: 10px; }
  .broker__square { width: 26px; height: 26px; background: var(--ink); }
  .broker__name { font-size: 22px; font-weight: 700; color: var(--ink); text-align: center; line-height: 27px; }
</style>
</head>
<body>
<main class="ad">
  <header class="brand">
    <span class="brand__square"></span>
    <div class="brand__name">
      <span class="brand__line">GRETA HASKINS &amp;</span>
      <span class="brand__line">LYDIA HASKINS MARLOW</span>
      <span class="brand__tag">REAL ESTATE</span>
    </div>
  </header>

  <section class="band">
    <h1 class="band__headline">Opportunity is knocking<br>Let us open the door</h1>
    <div class="agents">
      <div class="agent">
        <div class="agent__photo agent__photo--greta" role="img" aria-label="Portrait photo of Greta"></div>
        <p class="agent__name">GRETA:</p>
        <p class="agent__phone">(206) 555-0142</p>
      </div>
      <div class="agent">
        <div class="agent__photo agent__photo--lydia" role="img" aria-label="Portrait photo of Lydia"></div>
        <p class="agent__name">LYDIA:</p>
        <p class="agent__phone">(206) 555-0187</p>
      </div>
    </div>
  </section>

  <p class="tagline">Your trusted Mercer Island<br>real estate team for more<br>than 40 years.</p>

  <div class="contact">
    <p>info@gretaandlydia.com</p>
    <p>www.gretaandlydia.com</p>
  </div>

  <div class="broker">
    <span class="broker__square"></span>
    <p class="broker__name">Fenwick Dalton Rusk</p>
  </div>
</main>
</body>
</html>
```